Redesign for Popular UK Town Website

We're looking for someone to redesign a website for a popular tourist town that's visited by over 250,000 people a year. We have a basic design frame in place and need someone to make it look more 'professional.'
We've created a temporary design layout to show you a general idea of what we're looking for: http://dorrin.co.uk/
All text/images are placeholder images so you can get an idea of the general layout.
(Please note that you can grab any images found on the internet for 'tenby' to be used as placeholder images. This is because we will be visiting the locations and taking our own photos, after the design is complete.)
Target Market(s)
Tourists
Industry/Entity Type
Town
Number of Pages Required
2 page
Requirements
Must have
- You need to redesign the homepage: http://dorrin.co.uk/
- You also need to redesign the following page: http://dorrin.co.uk/hotels/ (This page will be used for multiple categories and is used to list locations of properties/places etc.)
- Design must be responsive also.
Nice to have
- Please feel free to add as much as you can to the content/features as with our limited knowledge of websites, have only been able to create a basic layout.

```html
<!DOCTYPE html>
<html lang="en">
<head>
<meta charset="utf-8">
<title>Hotels – Dorrin</title>
<link href="https://fonts.googleapis.com/css2?family=Montserrat:wght@400;500;600&family=Roboto:wght@400;500&family=Kaushan+Script&display=swap" rel="stylesheet">
<style>
:root{
  --accent:#1a9fe0;
  --ink:#222831;
  --text:#555b63;
  --muted:#9aa0a6;
  --page:#f4f4f4;
  --card:#ffffff;
  --line:#e6e6e6;
  --footer:#0d3a5e;
  --footer-dark:#0a2e4b;
  --white:#ffffff;
}
*{box-sizing:border-box;margin:0;padding:0}
html,body{width:710px;height:1200px;overflow:hidden}
body{font-family:'Roboto',sans-serif;color:var(--text);background:var(--white);position:relative}
a{color:inherit;text-decoration:none}

/* hero */
.hero{position:absolute;left:0;top:0;width:710px;height:151px;overflow:hidden}
.hero-photo{position:absolute;inset:0;background:
  linear-gradient(90deg,rgba(0,0,0,.15),rgba(0,0,0,.05) 50%,rgba(0,0,0,.2)),
  linear-gradient(180deg,#3b6f86 0%,#2f7f8c 35%,#4f7a4a 70%,#3d5b33 100%)}
.hero-photo::after{content:"";position:absolute;right:0;top:0;width:330px;height:151px;background:linear-gradient(180deg,#8d8a86,#b7ada2 50%,#6f6960);opacity:.75}
.hero-shade{position:absolute;inset:0;background:rgba(10,30,45,.25)}
.topbar{position:absolute;left:53px;right:52px;top:12px;display:flex;justify-content:space-between;align-items:center}
.brand{display:flex;align-items:center;gap:5px;color:var(--white)}
.brand-dot{width:20px;height:20px;border-radius:50%;background:var(--white)}
.brand-name{font-family:'Montserrat',sans-serif;font-weight:600;font-size:10px;line-height:1}
.brand-tag{font-size:3.5px;letter-spacing:.3px;margin-top:2px;display:block}
.nav{display:flex;gap:17px;font-family:'Montserrat',sans-serif;font-size:6.2px;font-weight:500;color:var(--white);text-transform:uppercase}
.nav a{position:relative}
.nav a.active::before{content:"";position:absolute;left:0;right:0;top:-12px;height:1.5px;background:var(--white)}
.hero-title{position:absolute;left:0;right:0;top:62px;text-align:center;font-family:'Kaushan Script',cursive;font-size:29px;color:var(--white)}
.breadcrumb{position:absolute;left:0;right:0;top:103px;text-align:center;font-family:'Montserrat',sans-serif;font-size:6.4px;color:var(--white);text-transform:uppercase}
.breadcrumb span{margin:0 6px}

/* listings */
.listings{position:absolute;left:0;top:151px;width:710px;height:634px;background:var(--page)}
.section-title{text-align:center;font-family:'Montserrat',sans-serif;font-weight:500;color:var(--ink)}
.section-title::after{content:"";display:block;width:19px;height:1.5px;background:var(--accent);margin:5px auto 0}
.listings .section-title{margin-top:29px;font-size:17px}
.grid{position:absolute;left:53px;top:67px;width:605px;display:grid;grid-template-columns:repeat(3,196px);grid-auto-rows:246px;column-gap:8.5px;row-gap:12px}
.card{background:var(--card);position:relative}
.card-photo{height:113px}
.card-body{padding:13px 12px 0}
.card-name{font-family:'Montserrat',sans-serif;font-weight:500;font-size:11.5px;color:var(--ink)}
.card-name::after{content:"";display:block;width:13px;height:1px;background:var(--line);margin:5px 0 0}
.card-address{display:flex;align-items:center;gap:3px;font-size:6.8px;color:var(--ink);margin-top:8px}
.card-info{margin-top:11px;font-size:6.8px;line-height:16px}
.card-more{position:absolute;left:12px;top:225px;font-family:'Montserrat',sans-serif;font-size:6.4px;font-weight:500;color:var(--accent);display:flex;align-items:center;gap:4px}
.pager{position:absolute;left:0;right:0;top:595px;display:flex;justify-content:center;align-items:center;font-size:6.8px;color:var(--text)}
.pager a{display:flex;align-items:center;justify-content:center;width:29px;height:18px}
.pager .wide{width:42px}
.pager .current{background:var(--accent);color:var(--white);border-radius:9px;width:25px;margin:0 2px}

/* tweets */
.tweets{position:absolute;left:0;top:785px;width:710px;height:252px;background:var(--white)}
.tweets .section-title{margin-top:23px;font-size:15.5px}
.tweets .section-title::after{margin-top:19px}
.tweets-by{position:absolute;left:0;right:0;top:44px;text-align:center;font-size:7px;color:var(--text)}
.tweet-row{position:absolute;left:53px;top:78px;display:grid;grid-template-columns:repeat(4,142px);column-gap:12.5px}
.tweet{height:138px;border:1px solid #eeeeee;box-shadow:0 1px 3px rgba(0,0,0,.05);padding:22px 18px 0}
.tweet-text{font-size:6.8px;line-height:13px;color:var(--text)}
.tweet-text b{font-weight:400;color:var(--accent)}
.tweet-author{display:flex;align-items:center;gap:10px;margin-top:18px}
.avatar{width:32px;height:32px;border-radius:50%;background:linear-gradient(135deg,#9aa3ab,#5e6770)}
.author-name{font-size:7.5px;font-weight:500;color:var(--ink)}
.author-handle{font-size:5.8px;color:var(--muted);margin-top:2px;font-style:italic}

/* footer */
.footer{position:absolute;left:0;top:1037px;width:710px;height:134px;background:var(--footer);color:var(--white)}
.footer-col{position:absolute;top:33px}
.footer-col h3{font-family:'Montserrat',sans-serif;font-weight:500;font-size:9.5px;margin-bottom:9px}
.footer-col p,.footer-col li{font-size:6.8px;line-height:13.2px;list-style:none}
.footer-col li{display:flex;align-items:center;gap:5px}
.pay{font-family:'Roboto',sans-serif;font-weight:500;font-size:9px;margin-top:5px}
.social-dot{width:4px;height:4px;background:var(--white);border-radius:1px}
.copy{position:absolute;left:0;top:1171px;width:710px;height:29px;background:var(--footer-dark);color:var(--white);font-size:6.8px;padding:9px 0 0 53px}
.to-top{position:absolute;left:672px;top:1160px;width:23px;height:23px;border-radius:50%;background:var(--accent);display:flex;align-items:center;justify-content:center}
</style>
</head>
<body>

<header class="hero">
  <div class="hero-photo" role="img" aria-label="Aerial view of the harbour town with sea, green headland and colourful houses"></div>
  <div class="hero-shade"></div>
  <div class="topbar">
    <a class="brand" href="http://dorrin.co.uk/">
      <span class="brand-dot"></span>
      <span class="brand-name">Harbourline<span class="brand-tag">YOUR COASTAL TOWN GUIDE</span></span>
    </a>
    <nav class="nav">
      <a href="#">Where to stay</a>
      <a href="#">Caravan and camping</a>
      <a href="#">Bed and breakfast</a>
      <a class="active" href="http://dorrin.co.uk/hotels/">Hotels</a>
      <a href="#">Contact us</a>
    </nav>
  </div>
  <h1 class="hero-title">Hotels</h1>
  <div class="breadcrumb">Home<span>&gt;</span>Hotels</div>
</header>

<main class="listings">
  <h2 class="section-title">Things to do</h2>
  <div class="grid">
    <article class="card">
      <div class="card-photo" role="img" aria-label="Pale blue hotel facade with flags" style="background:linear-gradient(180deg,#9ab8c0,#6f9097)"></div>
      <div class="card-body">
        <h3 class="card-name">Seawall Hotel</h3>
        <p class="card-address"><svg width="6" height="7" viewBox="0 0 6 7"><path d="M3 0a2.4 2.4 0 0 0-2.4 2.4C.6 4.2 3 7 3 7s2.4-2.8 2.4-4.6A2.4 2.4 0 0 0 3 0zm0 3.3a.9.9 0 1 1 0-1.8.9.9 0 0 1 0 1.8z" fill="#444"/></svg>Some address line goes here..</p>
        <p class="card-info">Telephone Number: 01632 960101<br>Email: stay@seawall-hotel.co.uk<br>Official website: http://www.seawall-hotel.co.uk/</p>
      </div>
      <a class="card-more" href="#">MORE <svg width="6" height="5" viewBox="0 0 6 5"><path d="M0 2.5h5M3.2.7 5 2.5 3.2 4.3" stroke="#1a9fe0" fill="none" stroke-width=".8"/></svg></a>
    </article>
    <article class="card">
      <div class="card-photo" role="img" aria-label="White hotel entrance with columns and trees" style="background:linear-gradient(120deg,#e9e7e2,#c9c6bd 60%,#4f7a45)"></div>
      <div class="card-body">
        <h3 class="card-name">The Meadow Hotel</h3>
        <p class="card-address"><svg width="6" height="7" viewBox="0 0 6 7"><path d="M3 0a2.4 2.4 0 0 0-2.4 2.4C.6 4.2 3 7 3 7s2.4-2.8 2.4-4.6A2.4 2.4 0 0 0 3 0zm0 3.3a.9.9 0 1 1 0-1.8.9.9 0 0 1 0 1.8z" fill="#444"/></svg>Some address line goes here..</p>
        <p class="card-info">Telephone Number: 01632 960102<br>Email: desk@meadowhoteldorrin.com<br>Official website: http://meadowhoteldorrin.com/</p>
      </div>
      <a class="card-more" href="#">MORE <svg width="6" height="5" viewBox="0 0 6 5"><path d="M0 2.5h5M3.2.7 5 2.5 3.2 4.3" stroke="#1a9fe0" fill="none" stroke-width=".8"/></svg></a>
    </article>
    <article class="card">
      <div class="card-photo" role="img" aria-label="White terraced hotel with bay windows" style="background:linear-gradient(180deg,#e8e8e6,#c8c8c4)"></div>
      <div class="card-body">
        <h3 class="card-name">The Headland Rise Hotel</h3>
        <p class="card-address"><svg width="6" height="7" viewBox="0 0 6 7"><path d="M3 0a2.4 2.4 0 0 0-2.4 2.4C.6 4.2 3 7 3 7s2.4-2.8 2.4-4.6A2.4 2.4 0 0 0 3 0zm0 3.3a.9.9 0 1 1 0-1.8.9.9 0 0 1 0 1.8z" fill="#444"/></svg>Some address line goes here..</p>
        <p class="card-info">Telephone Number: 01632 960103<br>Email: http://www.headlandrisehotel.com/</p>
      </div>
      <a class="card-more" href="#">MORE <svg width="6" height="5" viewBox="0 0 6 5"><path d="M0 2.5h5M3.2.7 5 2.5 3.2 4.3" stroke="#1a9fe0" fill="none" stroke-width=".8"/></svg></a>
    </article>
    <article class="card">
      <div class="card-photo" role="img" aria-label="Cream hotel with green balconies" style="background:linear-gradient(180deg,#ecebe6,#c9cbc0 70%,#5f7f5a)"></div>
      <div class="card-body">
        <h3 class="card-name">Linden House Hotel</h3>
        <p class="card-address"><svg width="6" height="7" viewBox="0 0 6 7"><path d="M3 0a2.4 2.4 0 0 0-2.4 2.4C.6 4.2 3 7 3 7s2.4-2.8 2.4-4.6A2.4 2.4 0 0 0 3 0zm0 3.3a.9.9 0 1 1 0-1.8.9.9 0 0 1 0 1.8z" fill="#444"/></svg>Some address line goes here..</p>
        <p class="card-info">Telephone Number:&nbsp; 01632 960104<br>Email: info@lindenhouse-dorrin.co.uk<br>Official website: www.lindenhouse-dorrin.co.uk/</p>
      </div>
      <a class="card-more" href="#">MORE <svg width="6" height="5" viewBox="0 0 6 5"><path d="M0 2.5h5M3.2.7 5 2.5 3.2 4.3" stroke="#1a9fe0" fill="none" stroke-width=".8"/></svg></a>
    </article>
    <article class="card">
      <div class="card-photo" role="img" aria-label="White hotel on a street corner under blue sky" style="background:linear-gradient(180deg,#7fa6cf,#d9d9d6 50%,#6b6b6b)"></div>
      <div class="card-body">
        <h3 class="card-name">The Kestrel Hotel</h3>
        <p class="card-address"><svg width="6" height="7" viewBox="0 0 6 7"><path d="M3 0a2.4 2.4 0 0 0-2.4 2.4C.6 4.2 3 7 3 7s2.4-2.8 2.4-4.6A2.4 2.4 0 0 0 3 0zm0 3.3a.9.9 0 1 1 0-1.8.9.9 0 0 1 0 1.8z" fill="#444"/></svg>Some address line goes here..</p>
        <p class="card-info">Telephone Number: 01632 960105<br>Email:&nbsp; kestreldorrin@mailnet.com<br>Official website: thekestreldorrin.com/</p>
      </div>
      <a class="card-more" href="#">MORE <svg width="6" height="5" viewBox="0 0 6 5"><path d="M0 2.5h5M3.2.7 5 2.5 3.2 4.3" stroke="#1a9fe0" fill="none" stroke-width=".8"/></svg></a>
    </article>
    <article class="card">
      <div class="card-photo" role="img" aria-label="Yellow seafront hotel under blue sky" style="background:linear-gradient(180deg,#3f6fb5,#d8c07a 45%,#c9b06a)"></div>
      <div class="card-body">
        <h3 class="card-name">Tideway Hotel</h3>
        <p class="card-address"><svg width="6" height="7" viewBox="0 0 6 7"><path d="M3 0a2.4 2.4 0 0 0-2.4 2.4C.6 4.2 3 7 3 7s2.4-2.8 2.4-4.6A2.4 2.4 0 0 0 3 0zm0 3.3a.9.9 0 1 1 0-1.8.9.9 0 0 1 0 1.8z" fill="#444"/></svg>Some address line goes here..</p>
        <p class="card-info">Telephone Number: 01632 960106<br>Email: hello@tideway-hotel.uk.com<br>Official website: www.tideway-hotel.uk.com/</p>
      </div>
      <a class="card-more" href="#">MORE <svg width="6" height="5" viewBox="0 0 6 5"><path d="M0 2.5h5M3.2.7 5 2.5 3.2 4.3" stroke="#1a9fe0" fill="none" stroke-width=".8"/></svg></a>
    </article>
  </div>
  <nav class="pager">
    <a class="wide" href="#">&lsaquo; PREV</a>
    <a href="#">1</a><a href="#">····</a><a href="#">3</a><a href="#">4</a>
    <a class="current" href="#">5</a>
    <a href="#">6</a><a href="#">7</a><a href="#">····</a><a href="#">94</a>
    <a class="wide" href="#">NEXT &rsaquo;</a>
  </nav>
</main>

<section class="tweets">
  <h2 class="section-title">Tweets</h2>
  <p class="tweets-by">by @DorrinOfficial</p>
  <div class="tweet-row">
    <article class="tweet">
      <p class="tweet-text">In enim justo rhoncus ut imper-diet a venenatis vitae justo nullam dictum felis eu pede mollis <b>#dorrin</b></p>
      <div class="tweet-author"><div class="avatar" role="img" aria-label="Profile photo"></div><div><p class="author-name">Ned Harlow</p><p class="author-handle">@ned</p></div></div>
    </article>
    <article class="tweet">
      <p class="tweet-text">In enim justo rhoncus ut imper-diet a venenatis vitae justo nullam dictum felis eu pede mollis <b>#dorrin</b></p>
      <div class="tweet-author"><div class="avatar" role="img" aria-label="Profile photo" style="background:linear-gradient(135deg,#e4e1dc,#a9a39b)"></div><div><p class="author-name">Owen Price</p><p class="author-handle">@owen</p></div></div>
    </article>
    <article class="tweet">
      <p class="tweet-text">In enim justo rhoncus ut imper-diet a venenatis vitae justo nullam dictum felis eu pede mollis <b>#dorrin</b></p>
      <div class="tweet-author"><div class="avatar" role="img" aria-label="Profile photo" style="background:linear-gradient(135deg,#d9c3a5,#4aa3c8)"></div><div><p class="author-name">Rosa Vale</p><p class="author-handle">@rosa</p></div></div>
    </article>
    <article class="tweet">
      <p class="tweet-text">In enim justo rhoncus ut imper-diet a venenatis vitae justo nullam dictum felis eu pede mollis <b>#dorrin</b></p>
      <div class="tweet-author"><div class="avatar" role="img" aria-label="Profile photo" style="background:linear-gradient(135deg,#cfd6db,#5a6470)"></div><div><p class="author-name">Ivor Lane</p><p class="author-handle">@ivor</p></div></div>
    </article>
  </div>
</section>

<footer class="footer">
  <div class="footer-col" style="left:53px">
    <h3>About Us</h3>
    <p>Lorem ipsum dolor sit amet, consectetuer adipiscing elit.<br>Aenean commodo ligula eget dolor aenean massa.<br>Cum sociis natoque penatibus .</p>
    <p class="pay">PayWell</p>
  </div>
  <div class="footer-col" style="left:289px">
    <h3>Informations</h3>
    <ul><li>About us</li><li>Sitemap</li><li>Advanced Search</li><li>Bookings</li><li>Contact</li></ul>
  </div>
  <div class="footer-col" style="left:426px">
    <h3>My Account</h3>
    <ul><li>Log In</li><li>View bookings</li><li>My wish list</li><li>Track My Tour</li><li>Help</li></ul>
  </div>
  <div class="footer-col" style="left:556px">
    <h3>Follow us</h3>
    <ul><li><span class="social-dot"></span>Gatherly</li><li><span class="social-dot"></span>Chirper</li><li><span class="social-dot"></span>Searchly +</li><li><span class="social-dot"></span>Snapgram</li></ul>
  </div>
</footer>
<div class="copy">© 2017, All Rights Reserved.</div>
<a class="to-top" href="#" aria-label="Back to top"><svg width="8" height="9" viewBox="0 0 8 9"><path d="M4 8.5V1M1 4 4 1l3 3" stroke="#fff" fill="none" stroke-width="1"/></svg></a>

</body>
</html>
```